Boutique High End Custom Furniture Store, Client Appreciation Card

We are looking to create a 5 x 7 card for our best clients that offer a 15% discount on their next furniture purchase. We would like to use both sides, full colour.

We are a high-end boutique furniture store located in Calgary, AB, Canada.

I have attached a card we did for our grand reopening that we like -- it's fresh with lots of white space. I have attached the image we used as well as a possible second image of furniture.

I have also attached other examples -- all seem fresh and clean with a layer of luxury.

I have attached all versions of our logo in an EPS file.

Target Market(s)

High disposable income, women over 40 who love style, contemporary design and fine art. Think Lila Morrow, Finn Ashby, Rue Dalston perfume and http://www.marlowquinby.example/

Industry/Entity Type

Boutique

Font styles to use
Sans Serif
Script

Colors
33a6d7
0592cd
85cae6
eda3c7
e667a6

Requirements
Must have
• Must be colour on both side (one side logo perhaps), the other side has content? Card needs to be 5 x 7 (either orientation is okay). Card needs to be fresh, stylish and current with the use of colour i.e. not all black and white. Logo needs to be prominent on either side.
• Please also have a look at our website.
Should not have
• Should not feel traditional or dated but at the same time not too playful so that it looks unprofessional. We are not "Gil's bargain Couches"!

```html
<!DOCTYPE html>
<html lang="en">
<head>
<meta charset="utf-8">
<title>Maison Verity – Client Appreciation Card</title>
<link rel="stylesheet" href="https://fonts.googleapis.com/css2?family=Questrial&family=Raleway:wght@100;300&display=swap">
<style>
  :root {
    --backdrop: #03abc6;
    --paper: #fbfcfd;
    --ink-grey: #6e6e70;
    --soft-grey: #9a9a9c;
    --rose: #ef8e9c;
    --rose-light: #f3a6b2;
    --rose-fade: #f7c3cb;
    --teal: #3bc3cf;
    --teal-fade: #c6eef1;
    --photo-top: #ffffff;
    --photo-mid: #f2f4f5;
    --photo-floor: #e4e5e6;
  }
  * { box-sizing: border-box; margin: 0; padding: 0; }
  html, body { width: 1200px; height: 859px; overflow: hidden; }
  body { background: var(--backdrop); position: relative; font-family: "Questrial", sans-serif; }

  .card { position: absolute; top: 70px; width: 514px; height: 719px; background: var(--paper); overflow: hidden; }
  .card--info { left: 72px; }
  .card--offer { left: 614px; }

  /* Brand name block */
  .brand { position: absolute; text-align: center; color: var(--ink-grey); font-family: "Questrial", sans-serif; }
  .brand__mark { display: block; margin: 0 auto; background: var(--rose); }
  .brand__name { text-transform: uppercase; line-height: 1; }
  .brand__line { line-height: 1; color: var(--soft-grey); }

  .card--info .brand { top: 96px; left: 0; right: 0; }
  .card--info .brand__mark { width: 16px; height: 16px; margin-bottom: 40px; }
  .card--info .brand__name { font-size: 29px; letter-spacing: 2px; }
  .card--info .brand__line { font-size: 14px; margin-top: 12px; }

  .rule { position: absolute; top: 227px; left: 190px; width: 135px; height: 1px; background: var(--rose); }

  .about { position: absolute; top: 254px; left: 0; right: 0; text-align: center; font-size: 23px; line-height: 35px; letter-spacing: 2.9px; text-transform: uppercase; color: var(--ink-grey); white-space: nowrap; }

  .address-pill { position: absolute; left: 0; top: 563px; width: 242px; height: 60px; border-radius: 0 30px 30px 0; background: linear-gradient(90deg, var(--rose) 0%, var(--rose-light) 70%, var(--rose-fade) 100%); color: #fff; font-family: "Raleway", sans-serif; font-weight: 300; font-size: 14px; line-height: 19px; padding: 12px 0 0 13px; text-transform: uppercase; letter-spacing: -0.4px; }

  .contact { position: absolute; left: 16px; top: 644px; font-family: "Raleway", sans-serif; font-weight: 300; font-size: 12.5px; line-height: 16px; color: var(--soft-grey); text-transform: uppercase; letter-spacing: -0.4px; }

  .spark { position: absolute; width: 24px; height: 24px; }
  .spark--a { left: 400px; top: 600px; }
  .spark--b { left: 450px; top: 628px; }
  .spark--c { left: 400px; top: 656px; }

  /* Offer side */
  .photo { position: absolute; inset: 0; background: linear-gradient(180deg, var(--photo-top) 0%, var(--photo-mid) 68%, var(--photo-floor) 100%); }

  .headline { position: absolute; font-family: "Raleway", sans-serif; font-weight: 100; color: var(--rose-light); font-size: 66px; line-height: 1; letter-spacing: 1px; text-transform: uppercase; }
  .headline--top { left: 38px; top: 104px; }
  .headline--bottom { right: 34px; top: 168px; }

  .offer-pill { position: absolute; right: 0; top: 300px; width: 242px; height: 60px; border-radius: 30px 0 0 30px; background: linear-gradient(90deg, var(--teal) 0%, #69d0d9 60%, var(--teal-fade) 100%); color: #fff; font-family: "Raleway", sans-serif; font-weight: 300; font-size: 17px; line-height: 24px; text-align: center; text-transform: uppercase; padding-top: 7px; letter-spacing: -0.2px; }
  .offer-pill small { font-size: 11px; }

  .terms { position: absolute; left: 272px; width: 212px; top: 400px; text-align: center; font-family: "Raleway", sans-serif; font-weight: 300; font-size: 11px; line-height: 14.5px; color: var(--soft-grey); text-transform: uppercase; white-space: nowrap; }
  .terms__star { color: var(--rose); }

  .card--offer .brand { top: 552px; left: 186px; width: 200px; }
  .card--offer .brand__mark { width: 10px; height: 10px; margin-bottom: 20px; background: var(--ink-grey); }
  .card--offer .brand__name { font-size: 19px; letter-spacing: 1.2px; }
  .card--offer .brand__line { font-size: 9px; margin-top: 6px; }
</style>
</head>
<body>
  <section class="card card--info">
    <div class="brand">
      <span class="brand__mark"></span>
      <div class="brand__name">Maison Verity</div>
      <div class="brand__line">Curated home interiors</div>
    </div>
    <div class="rule"></div>
    <p class="about">Maison Verity is a unique<br>boutique custom furniture<br>store offering a wide selec-<br>tion of furniture, rugs,<br>bedding, lighting, window<br>coverings, accessories and<br>interior design services.</p>
    <div class="address-pill">88 Larch Row SW, Calgary AB<br>403.555.0142</div>
    <div class="contact">info@maisonverity.example<br>maisonverity.example</div>
    <svg class="spark spark--a" viewBox="0 0 24 24" aria-hidden="true"><g stroke="#3bc3cf" stroke-width="4" stroke-linecap="round"><line x1="12" y1="2" x2="12" y2="22"/><line x1="3.3" y1="7" x2="20.7" y2="17"/><line x1="3.3" y1="17" x2="20.7" y2="7"/></g></svg>
    <svg class="spark spark--b" viewBox="0 0 24 24" aria-hidden="true"><g stroke="#3bc3cf" stroke-width="4" stroke-linecap="round"><line x1="12" y1="2" x2="12" y2="22"/><line x1="3.3" y1="7" x2="20.7" y2="17"/><line x1="3.3" y1="17" x2="20.7" y2="7"/></g></svg>
    <svg class="spark spark--c" viewBox="0 0 24 24" aria-hidden="true"><g stroke="#3bc3cf" stroke-width="4" stroke-linecap="round"><line x1="12" y1="2" x2="12" y2="22"/><line x1="3.3" y1="7" x2="20.7" y2="17"/><line x1="3.3" y1="17" x2="20.7" y2="7"/></g></svg>
  </section>

  <section class="card card--offer">
    <div class="photo" role="img" aria-label="Bright white room photograph with a turquoise upholstered bench on a silver base, a black pedestal side table with books and a vase of turquoise eucalyptus"></div>
    <div class="headline headline--top">Our Gift</div>
    <div class="headline headline--bottom">To You</div>
    <div class="offer-pill">Enjoy 15<small>%</small><br>Off at Maison Verity</div>
    <p class="terms"><span class="terms__star">*</span> Offer is good for one-time use<br>and cannot be combined with<br>other offers.</p>
    <div class="brand">
      <span class="brand__mark"></span>
      <div class="brand__name">Maison Verity</div>
      <div class="brand__line">Curated home interiors</div>
    </div>
  </section>
</body>
</html>
```